TheHarborKeyway.com (Luxury Business Card Design)

I’m looking for assistance with design. I have a clear vision in mind, but I need help translating it into a properly formatted file for print.
Ideally, I’d like to work directly with a designer to communicate my vision and finalize the design in the correct vector format required for submission to a printing company. I already have some examples I've created just need someone with design experience to help me do the finishing touches

Target Market(s)

Real Estate

Industry/Entity Type

Real Estate

Contact Information for Business Card

the name of the company, QR code, my The harbor keyway email. Owner/founder title.

Font styles to use
Decorative
Script

Requirements
Must have
• vector for printing company
Nice to have
• I am set on a black and gold design, and will be using a gold foiling. QR code to be done in a gold foiling or inlay.
Should not have
• wild colors I want black and gold, please see my pdf examples.

```html
<!DOCTYPE html>
<html lang="en">
<head>
<meta charset="utf-8">
<title>The Harbor Keyway – Business Card</title>
<link rel="stylesheet" href="https://fonts.googleapis.com/css2?family=Jim+Nightshade&family=Cormorant+Garamond:ital,wght@1,600&family=Tinos&display=swap">
<style>
  :root {
    --page: #e4e4e4;
    --card-black: #0a0b0d;
    --gold: #a8742a;
    --ink: #151515;
  }
  html, body {
    margin: 0;
    padding: 0;
    width: 1200px;
    height: 1200px;
    overflow: hidden;
    background: var(--page);
  }
  .canvas {
    position: relative;
    width: 1200px;
    height: 1200px;
  }
  .card {
    position: absolute;
    left: 169px;
    width: 862px;
    height: 506px;
    background: var(--card-black);
    overflow: hidden;
  }
  .card--front { top: 71px; }
  .card--back { top: 631px; }
  .card svg.panel {
    position: absolute;
    inset: 0;
    width: 100%;
    height: 100%;
  }
  .ornament {
    position: absolute;
    width: 144px;
    height: 146px;
  }
  .ornament--tl { left: 37px; top: 39px; }
  .ornament--tr { left: 681px; top: 39px; }
  .ornament--bl { left: 37px; top: 322px; }
  .ornament--br { left: 681px; top: 322px; }
  .ornament rect { fill: var(--gold); opacity: 0.42; }
  .front-text {
    position: absolute;
    left: 0;
    width: 100%;
    text-align: center;
    margin: 0;
    color: var(--ink);
    line-height: 1;
    white-space: nowrap;
  }
  .brand-name {
    font-family: "Jim Nightshade", cursive;
    font-size: 46px;
    letter-spacing: 5px;
    top: 134px;
  }
  .person-name {
    font-family: "Cormorant Garamond", serif;
    font-style: italic;
    font-weight: 600;
    font-size: 50px;
    top: 198px;
  }
  .person-title {
    font-family: "Tinos", serif;
    font-size: 20px;
    top: 254px;
  }
  .contact-icons {
    position: absolute;
    top: 302px;
    left: 0;
    width: 100%;
    display: flex;
    justify-content: center;
    gap: 14px;
  }
  .contact-icons svg { width: 16px; height: 16px; }
  .contact-line {
    font-family: "Tinos", serif;
    font-size: 21px;
  }
  .contact-phone { top: 337px; }
  .contact-email { top: 370px; }
  .contact-web { top: 404px; }
  .back-art {
    position: absolute;
    inset: 0;
    width: 100%;
    height: 100%;
  }
  .back-brand {
    position: absolute;
    left: 201px;
    width: 600px;
    top: 290px;
    margin: 0;
    text-align: center;
    white-space: nowrap;
    font-family: "Jim Nightshade", cursive;
    font-size: 66px;
    letter-spacing: 7px;
    line-height: 1;
    color: var(--gold);
  }
</style>
</head>
<body>
<main class="canvas">

  <section class="card card--front" aria-label="Business card front">
    <svg class="panel" viewBox="0 0 690 405" preserveAspectRatio="none" aria-hidden="true">
      <path fill="var(--gold)" d="M202 31 L487 31 Q505 185 660 203 Q505 221 487 375 L202 375 Q184 221 35 203 Q184 185 202 31 Z"/>
    </svg>

    <svg class="ornament ornament--tl" viewBox="0 0 144 146" role="img" aria-label="Gold flourish with swirls and leaves">
      <rect x="92" y="6" width="40" height="134" rx="20"/>
      <rect x="6" y="100" width="126" height="40" rx="20"/>
    </svg>
    <svg class="ornament ornament--tr" viewBox="0 0 144 146" role="img" aria-label="Gold flourish with swirls and leaves">
      <rect x="12" y="6" width="40" height="134" rx="20"/>
      <rect x="12" y="100" width="126" height="40" rx="20"/>
    </svg>
    <svg class="ornament ornament--bl" viewBox="0 0 144 146" role="img" aria-label="Gold flourish with swirls and leaves">
      <rect x="92" y="6" width="40" height="134" rx="20"/>
      <rect x="6" y="6" width="126" height="40" rx="20"/>
    </svg>
    <svg class="ornament ornament--br" viewBox="0 0 144 146" role="img" aria-label="Gold flourish with swirls and leaves">
      <rect x="12" y="6" width="40" height="134" rx="20"/>
      <rect x="12" y="6" width="126" height="40" rx="20"/>
    </svg>

    <p class="front-text brand-name">The Harbor Keyway</p>
    <p class="front-text person-name">Your Name</p>
    <p class="front-text person-title">Designation</p>

    <div class="contact-icons" aria-hidden="true">
      <svg viewBox="0 0 16 16"><path fill="var(--ink)" d="M3 1.5l2.5 0 1 3.5-1.6 1.2a9 9 0 0 0 4.9 4.9L11 9.5l3.5 1v2.5c0 .8-.7 1.5-1.5 1.5A12.5 12.5 0 0 1 1.5 3C1.5 2.2 2.2 1.5 3 1.5z"/></svg>
      <svg viewBox="0 0 16 16"><rect x="1.5" y="3.5" width="13" height="9" fill="var(--ink)"/><path d="M1.5 3.5 8 8.5l6.5-5" fill="none" stroke="var(--gold)" stroke-width="1.2"/></svg>
      <svg viewBox="0 0 16 16"><circle cx="8" cy="8" r="6.5" fill="var(--ink)"/><path d="M1.5 8h13M8 1.5c-3 3.5-3 9.5 0 13M8 1.5c3 3.5 3 9.5 0 13" fill="none" stroke="var(--gold)" stroke-width="1"/></svg>
    </div>
    <p class="front-text contact-line contact-phone">(123) 123-4567</p>
    <p class="front-text contact-line contact-email">info@theharborkeyway.com</p>
    <p class="front-text contact-line contact-web">theharborkeyway.com</p>
  </section>

  <section class="card card--back" aria-label="Business card back">
    <svg class="back-art" viewBox="0 0 862 506" aria-hidden="true">
      <path d="M0 2H503M2 0V506" stroke="var(--gold)" stroke-width="4" fill="none"/>
    </svg>
    <svg class="back-art" viewBox="0 0 862 506" role="img" aria-label="Gold corner vine with leaves and swirls">
      <path fill="var(--gold)" opacity="0.45" d="M18 18 H490 Q470 70 360 96 Q230 120 170 150 Q118 190 112 290 Q108 410 100 490 H18 Z"/>
    </svg>
    <p class="back-brand">The Harbor Keyway</p>
  </section>

</main>
</body>
</html>
```